Outdoor Street Sign in front of Commercial Building

I need a street sign roughly 4 feet tall and 6 feet wide. The sign will say “ PAINTLESS DENT REPAIR “. I need this sign to stand out and look Professional. I will provide photos of my shop and the location of this future sign. Color Scheme is very important to me.

Target Market(s)

People who own vehicles with Door Dings

Industry/Entity Type

Cosmetic Automobile Restoration

Font styles to use
Sans Serif
Other font styles liked:
• Gravity Normal, Kairos display solid, LTC square face small,

Colors

Designer to choose colors to be used in the design.

Requirements
Must have
• This street sign is simple in that it just needs to say “ PAINTLESS DENT REPAIR “. It is the creativity of the sign that is important to me. My commercial shop is on a busy street with a lot of traffic. My building really stands out and everyone can see my Company Name, which is Larkmoor Dent Repair. I need this sign to distinguish me from conventional body shops with the phrase “ PAINTLESS DENT REPAIR “. The whole point of this sign is for people driving by to do their own research on what Paintless Dent Repair is ?? If you can incorporate the same honeycomb pattern / design that is used as the background of my building sign, that would be great !!
Nice to have
• I’d like to see my company colors, which are red, black, and silver. Please be creative to somehow make this stand out. It would be nice to have the same honeycomb pattern / design that’s used as the background on the building sign to be used as the background of this sign !
Should not have
• This sign does not need any other information on it. Only the phrase “ PAINTLESS DENT REPAIR “

```html
<!DOCTYPE html>
<html lang="en">
<head>
<meta charset="utf-8">
<title>Paintless Dent Repair – Street Sign</title>
<link href="https://fonts.googleapis.com/css2?family=Exo+2:ital,wght@0,800;1,800;1,900&family=Russo+One&display=swap" rel="stylesheet">
<style>
  :root {
    --backdrop: #bdbdbd;
    --sign-black: #0b0d12;
    --photo-dark: #1a1c22;
    --brand-red: #ed1c24;
    --deep-red: #9e0d12;
    --silver-light: #f4f4f4;
    --silver-mid: #b9bbbe;
    --silver-dark: #8d8f93;
    --white: #ffffff;
    --ink: #0a0a0a;
  }
  * { box-sizing: border-box; margin: 0; padding: 0; }
  html, body {
    width: 1200px; height: 1200px; overflow: hidden;
    background: var(--backdrop);
  }
  .sign {
    position: absolute;
    left: 75px; top: 250px;
    width: 1051px; height: 700px;
    background: var(--sign-black);
    overflow: hidden;
  }
  .shop-photo {
    position: absolute; left: 0; top: 0; width: 100%; height: 619px;
    background:
      radial-gradient(ellipse 45% 55% at 18% 45%, #2a262a 0%, rgba(26,28,34,0) 100%),
      linear-gradient(180deg, var(--sign-black) 0%, var(--photo-dark) 55%, #121316 100%);
  }
  .rule {
    position: absolute; left: 61px; width: 925px; height: 1.5px;
    background: var(--silver-light);
  }
  .rule--top { top: 41px; }
  .rule--bottom { top: 113px; }
  .headline {
    position: absolute; left: 0; top: 45px; width: 100%;
    text-align: center;
    font-family: "Exo 2", sans-serif; font-style: italic; font-weight: 900;
    font-size: 72px; line-height: 66px; letter-spacing: 3px;
    text-transform: uppercase;
    white-space: nowrap;
  }
  .headline span {
    -webkit-background-clip: text; background-clip: text; color: transparent;
  }
  .headline .accent { background-image: linear-gradient(var(--brand-red) 50%, var(--deep-red)); }
  .headline .metal { background-image: linear-gradient(var(--white) 45%, var(--silver-dark)); }
  .brand-name {
    position: absolute; left: 0; top: 218px; width: 100%;
    text-align: center;
    font-family: "Exo 2", sans-serif; font-weight: 800;
    font-size: 100px; line-height: 104px; letter-spacing: 4px;
    color: var(--brand-red); text-transform: uppercase;
    white-space: nowrap;
  }
  .phone {
    position: absolute; left: 0; top: 515px; width: 100%;
    padding-left: 20px;
    text-align: center;
    font-family: "Russo One", sans-serif;
    font-size: 92px; line-height: 100px; letter-spacing: 20px;
    background-image: linear-gradient(var(--brand-red) 55%, var(--deep-red));
    -webkit-background-clip: text; background-clip: text; color: transparent;
    white-space: nowrap;
  }
  .web-band {
    position: absolute; left: 0; top: 619px; width: 100%; height: 81px;
    border-top: 8px solid var(--white);
    background: linear-gradient(90deg, var(--silver-light) 0%, var(--silver-mid) 25%, var(--silver-light) 50%, var(--silver-mid) 75%, var(--silver-dark) 100%);
    text-align: center;
  }
  .web-address {
    font-family: "Exo 2", sans-serif; font-style: italic; font-weight: 800;
    font-size: 57px; line-height: 72px; color: var(--ink);
    white-space: nowrap;
  }
</style>
</head>
<body>
  <div class="sign">
    <div class="shop-photo" role="img" aria-label="Darkened photo of the dent repair shop building at dusk"></div>
    <div class="rule rule--top"></div>
    <h1 class="headline"><span class="accent">Paintless</span> <span class="metal">Dent Repair</span></h1>
    <div class="rule rule--bottom"></div>
    <div class="brand-name">Larkmoor<br>Dent Repair</div>
    <div class="phone">555-214-7730</div>
    <div class="web-band">
      <div class="web-address">www.larkmoordentrepair.com</div>
    </div>
  </div>
</body>
</html>
```